Amber Ridge Partners Business Card

A business card design to accompany the logo design you completed on Pixel Forum. We are open to your proposals. I did add one idea below that might work, but we aren't married to the idea. The company is a real estate services company. Clientele are typically high net worth individuals, executive level employment or owners of their own company, 30-60 years old.

Our 1 (bad?) idea: double sided card; One side landscape with logo and word mark. Other side Portrait with the logo only (oversize watermark maybe?). Somewhere add text of Name (Marcus Tellingham), Title (Principal), phone # (555-214-7736) and email address (marcus@amberridgeco.example). There would be a second design with my wife's name, number and email in place of mine.

Again totally open to ideas here.

Industry/Entity Type

Real Estate

```html
<!DOCTYPE html>
<html lang="en">
<head>
<meta charset="utf-8">
<title>Amber Ridge Partners – Business Card</title>
<link rel="stylesheet" href="https://fonts.googleapis.com/css2?family=Cinzel:wght@400&family=Arimo:wght@400&display=swap">
<style>
  :root {
    --sage: #63944f;
    --paper: #ffffff;
    --backdrop: #727272;
    --card-shadow: rgba(0, 0, 0, 0.35);
  }
  * { margin: 0; padding: 0; box-sizing: border-box; }
  html, body {
    width: 1200px;
    height: 900px;
    overflow: hidden;
  }
  body {
    position: relative;
    background: radial-gradient(ellipse at 50% 40%, #8a8a8a 0%, var(--backdrop) 70%, #5e5e5e 100%);
    font-family: "Arimo", Arial, sans-serif;
  }
  .card {
    position: absolute;
    overflow: hidden;
    background: var(--paper);
    box-shadow: 2px 3px 6px var(--card-shadow);
  }
  .card-curve {
    position: absolute;
    inset: 0;
    width: 100%;
    height: 100%;
  }

  /* Portrait side: contact details */
  .card--portrait {
    left: 100px;
    top: 52px;
    width: 298px;
    height: 485px;
  }
  .brand {
    position: absolute;
    display: flex;
    align-items: center;
    color: var(--sage);
    font-family: "Cinzel", "Times New Roman", serif;
    font-weight: 400;
    line-height: 1.05;
  }
  .brand-dot {
    flex: none;
    border-radius: 50%;
    background: var(--sage);
  }
  .card--portrait .brand {
    left: 40px;
    top: 38px;
    gap: 14px;
    font-size: 19px;
  }
  .card--portrait .brand-dot { width: 42px; height: 42px; }

  .person {
    position: absolute;
    left: 0;
    right: 0;
    top: 226px;
    text-align: center;
    color: var(--paper);
  }
  .person-name {
    font-family: "Cinzel", "Times New Roman", serif;
    font-weight: 400;
    font-size: 20px;
    letter-spacing: 0.5px;
  }
  .person-title {
    margin-top: 6px;
    font-size: 13px;
  }
  .contact {
    position: absolute;
    left: 0;
    right: 0;
    top: 392px;
    list-style: none;
    text-align: center;
    color: var(--paper);
    font-size: 14px;
    line-height: 19px;
  }
  .contact li {
    display: flex;
    justify-content: center;
    align-items: center;
    gap: 5px;
  }
  .contact svg { width: 10px; height: 11px; }

  /* Landscape side: brand */
  .card--landscape {
    left: 517px;
    top: 52px;
    width: 485px;
    height: 297px;
  }
  .card--landscape .brand {
    left: 70px;
    top: 90px;
    gap: 20px;
    color: var(--paper);
    font-size: 34px;
  }
  .card--landscape .brand-dot {
    width: 64px;
    height: 64px;
    background: var(--paper);
  }
  .web {
    position: absolute;
    left: 0;
    right: 0;
    top: 198px;
    display: flex;
    justify-content: center;
    align-items: center;
    gap: 4px;
    color: var(--sage);
    font-size: 13px;
  }
  .web svg { width: 10px; height: 10px; }
</style>
</head>
<body>

  <section class="card card--portrait" aria-label="Business card, contact side">
    <svg class="card-curve" viewBox="0 0 298 485" preserveAspectRatio="none" aria-hidden="true">
      <path d="M0 190 Q149 120 298 190 L298 485 L0 485 Z" fill="var(--sage)"/>
    </svg>
    <div class="brand">
      <span class="brand-dot"></span>
      <span class="brand-name">Amber Ridge<br>Partners</span>
    </div>
    <div class="person">
      <p class="person-name">Marcus Tellingham</p>
      <p class="person-title">Principal</p>
    </div>
    <ul class="contact">
      <li>
        <svg viewBox="0 0 10 14" aria-hidden="true"><rect x="1.5" y="0.8" width="7" height="12.4" rx="1.2" fill="none" stroke="currentColor" stroke-width="1.2"/><line x1="4" y1="11" x2="6" y2="11" stroke="currentColor" stroke-width="1"/></svg>
        <span>555-214-7736</span>
      </li>
      <li>
        <svg viewBox="0 0 12 10" aria-hidden="true"><rect x="0.6" y="1.2" width="10.8" height="8" fill="none" stroke="currentColor" stroke-width="1.1"/><path d="M0.6 1.4 L6 5.8 L11.4 1.4" fill="none" stroke="currentColor" stroke-width="1.1"/></svg>
        <span>marcus@amberridgeco.example</span>
      </li>
    </ul>
  </section>

  <section class="card card--landscape" aria-label="Business card, brand side">
    <svg class="card-curve" viewBox="0 0 485 297" preserveAspectRatio="none" aria-hidden="true">
      <rect width="485" height="297" fill="var(--sage)"/>
      <path d="M0 255 Q242 115 485 255 L485 297 L0 297 Z" fill="var(--paper)"/>
    </svg>
    <div class="brand">
      <span class="brand-dot"></span>
      <span class="brand-name">Amber Ridge<br>Partners</span>
    </div>
    <p class="web">
      <svg viewBox="0 0 12 12" aria-hidden="true"><circle cx="6" cy="6" r="5.3" fill="none" stroke="currentColor" stroke-width="1.1"/><ellipse cx="6" cy="6" rx="2.3" ry="5.3" fill="none" stroke="currentColor" stroke-width="1"/><line x1="0.7" y1="6" x2="11.3" y2="6" stroke="currentColor" stroke-width="1"/></svg>
      <span>www.amberridgeco.example</span>
    </p>
  </section>

</body>
</html>
```